Posters for Sociology/Inequality exhibition

I need about 10 similarly themed A2 sized posters (so you don't need to do each one from scratch) for a Sociology exhibition on Inequality. The first half are general descriptions about Sociology, the second half, about inequality. They are meant to be educational to a university student audience.

We are from the Lantern Society. I have attached a file below about the write-up content for the various posters, do have a look and do your sample base on that. The write-up is not yet complete, so it may change. Likewise, the point form of the write-up are for reading only, I don't expect them to be in the poster.

Feel free to separate the points if you find them too wordy, because I do not have an idea how the poster will eventually look like. Try your best!

-

Note: There were some problems with the word file attached, but I have changed and fixed it already, do have a look at it!

Also, I need the posters by Saturday/Sunday so most probably I will award the winner before that. I need it done earlier than later because I still need to get it approved.

The size may be big but that's because I want it to be readable, rather than have too many things in it.

You don't have to do all the 10 different ones first, just start with some or a few, submit a sample, and we'll take it from there!

Please ask if you have any questions!

Hi everyone, post your samples (1 or a few) soon because I will have a make a decision soon, most probably by tomorrow. 

I know it's rushed but try your best.

Target Market(s)

18-28 years old students at an institute/university

Industry/Entity Type

University

Requirements
Must have
• 1. A consistent theme that runs throughout the posters.
2. Very Readable, Appealing Font
3. Visually appealing for an exhibition
Should not have
• Not be too overwhelming

```html
<!DOCTYPE html>
<html lang="en">
<head>
<meta charset="utf-8">
<title>Inequality – Lantern Society</title>
<link rel="stylesheet" href="https://fonts.googleapis.com/css2?family=Caveat:wght@400&family=Open+Sans:ital,wght@0,400;1,400;1,700&display=swap">
<style>
  :root {
    --poster-red: #d8271d;
    --paper-white: #ffffff;
    --note-light: #f7f7f7;
    --note-shade: #dcdcdc;
    --ink-dark: #111111;
    --ink-grey: #8a8a8a;
    --title-grey: #8c8c8c;
    --divider: #ef8a6a;
  }
  html, body {
    margin: 0;
    padding: 0;
    overflow: hidden;
    background: var(--paper-white);
  }
  .poster {
    position: relative;
    width: 848px;
    height: 1200px;
    overflow: hidden;
    background: var(--paper-white);
    font-family: "Open Sans", Arial, sans-serif;
  }
  .side-band {
    position: absolute;
    left: 85px;
    top: 0;
    width: 314px;
    height: 735px;
    background: var(--poster-red);
  }
  .publisher {
    position: absolute;
    top: 16px;
    right: 22px;
    margin: 0;
    font-size: 14px;
    font-style: italic;
    color: var(--ink-grey);
  }
  .pinned-note {
    position: absolute;
    left: 208px;
    top: 88px;
    width: 480px;
    height: 470px;
    transform: rotate(-2deg);
    background: linear-gradient(160deg, var(--note-light) 0%, #ececec 70%, var(--note-shade) 100%);
    box-shadow: 6px 8px 14px rgba(0,0,0,0.25);
  }
  .poster-title {
    position: absolute;
    left: 178px;
    top: 250px;
    width: 500px;
    margin: 0;
    display: flex;
    align-items: center;
    transform: rotate(-14deg);
    transform-origin: left center;
    font-family: "Caveat", "Comic Sans MS", cursive;
    font-weight: 400;
    font-size: 140px;
    line-height: 1;
    color: var(--title-grey);
  }
  .title-dash {
    display: inline-block;
    width: 70px;
    height: 3px;
    margin-right: 6px;
    margin-top: 30px;
    background: var(--title-grey);
  }
  .byline {
    position: absolute;
    right: 8px;
    top: 682px;
    margin: 0;
    font-size: 36px;
    line-height: 1;
    font-weight: 700;
    font-style: italic;
    color: var(--ink-dark);
    letter-spacing: -0.3px;
  }
  .info-panel {
    position: absolute;
    left: 0;
    top: 735px;
    width: 848px;
    height: 465px;
    background: var(--poster-red);
  }
  .points {
    list-style: none;
    margin: 0;
    padding: 0;
    position: absolute;
    left: 81px;
    top: 44px;
    width: 760px;
  }
  .point {
    position: relative;
    padding-left: 17px;
    color: var(--paper-white);
    font-size: 22.5px;
    font-style: italic;
    line-height: 34px;
  }
  .point::before {
    content: "";
    position: absolute;
    left: 0;
    top: 14px;
    width: 7px;
    height: 7px;
    background: var(--paper-white);
  }
  .point-rule {
    height: 1px;
    background: var(--divider);
    margin: 13px 0 11px 0;
  }
  .rule-short { width: 201px; }
  .rule-long { width: 387px; }
  .rule-mid { width: 248px; }
</style>
</head>
<body>
  <main class="poster">
    <div class="side-band"></div>
    <p class="publisher">Northfield Social Research Guild</p>

    <div class="pinned-note" role="img" aria-label="Paper note pinned to the wall with a blue pushpin"></div>

    <h1 class="poster-title"><span class="title-dash" aria-hidden="true"></span>inequality</h1>

    <p class="byline">by the Lantern Society...</p>

    <section class="info-panel">
      <ul class="points">
        <li class="point">Inequality is a broad and complex topic.</li>
        <li class="point-rule rule-short" aria-hidden="true"></li>
        <li class="point">It is a normative term, meaning to say, it involves value judgements. When we say there is inequality, we take it to mean that there are some things that are unequal, meaning to say, not the same between two or more comparisons. For instance income, health or access to knowledge.</li>
        <li class="point-rule rule-long" aria-hidden="true"></li>
        <li class="point">Thus, to describe something as unequal requires clarification, for we bring in our own subjective understandings of what is unequal and what we think should be equal.</li>
        <li class="point-rule rule-mid" aria-hidden="true"></li>
      </ul>
    </section>
  </main>
</body>
</html>
```